Upmarket building and construction company needs signage

Our building company R Brent Construction, needs signage to put up on the side of our vehicle trailers and on site fencing. We are a building company that specialises in residential construction and carpentry .

I will attach our logo and some inspirational pics for site fencing as well as what our trailer looks like .
Other details i would like on the sign are our
( email) rbrentconstruction@mailbox-example.net
(mobile ) 0493 518 264
(website ) rbrentconstruction. example.net

Target Market(s)

Home owners looking for a reliable local builder who produces good quality work. I have attached some inspirational pics.

Industry/Entity Type

Building and Construction

Colors

Designer to choose colors to be used in the design.

Requirements
Must have
• Our logo, contact information
Nice to have
• We would like the design to have elements of being Elegant, Serious, Modern, Professional, Masculine, Conservative and Upmarket.

```html
<!DOCTYPE html>
<html lang="en">
<head>
<meta charset="utf-8">
<title>R Brent Construction – Site Signage</title>
<link rel="stylesheet" href="https://fonts.googleapis.com/css2?family=Jost:wght@400;500;700&display=swap">
<style>
  :root {
    --backdrop: #a1a1a1;
    --charcoal: #373737;
    --bronze: #b07a25;
    --paper: #ffffff;
    --ink-grey: #666666;
    --white-text: #ffffff;
    --plan-tint: #f6efe4;
  }
  html, body {
    margin: 0;
    padding: 0;
    width: 1200px;
    height: 810px;
    overflow: hidden;
    background: var(--backdrop);
  }
  .sign {
    position: absolute;
    left: 50px;
    top: 92px;
    width: 1100px;
    height: 626px;
  }
  .sign svg { display: block; width: 1100px; height: 626px; }
  .service-item, .contact-line, .phone-number, .company-name {
    font-family: 'Jost', sans-serif;
  }
  .service-item { fill: var(--white-text); font-size: 35px; font-weight: 400; }
  .phone-number { fill: var(--white-text); font-size: 54px; font-weight: 700; }
  .contact-line { fill: var(--white-text); font-size: 22px; font-weight: 400; }
  .company-name { fill: var(--ink-grey); font-size: 64px; font-weight: 500; }
  .tick-icon { fill: none; stroke: var(--bronze); stroke-width: 3; stroke-linecap: round; stroke-linejoin: round; }
  .phone-icon { fill: var(--white-text); }
</style>
</head>
<body>
<div class="sign">
  <svg viewBox="0 0 1100 626" xmlns="http://www.w3.org/2000/svg">
    <defs>
      <linearGradient id="planWash" x1="0" y1="0" x2="1" y2="1">
        <stop offset="0" stop-color="#faf6ef"/>
        <stop offset="1" stop-color="#f6efe4"/>
      </linearGradient>
    </defs>

    <rect class="dark-panel" width="1100" height="626" fill="var(--charcoal)"/>
    <path class="bronze-sweep" d="M549 0 Q407 313 549 626 L1100 626 L1100 0 Z" fill="var(--bronze)"/>
    <path class="light-panel" d="M578 0 Q404 313 578 626 L1100 626 L1100 0 Z" fill="var(--paper)"/>
    <path class="plan-backdrop" role="img" aria-label="Faint architectural elevation drawing of a two-storey house"
          d="M578 0 Q404 313 578 626 L1100 626 L1100 0 Z" fill="url(#planWash)" opacity="0.7"/>

    <g class="service-list">
      <g transform="translate(64,76)">
        <rect class="tick-icon" x="0" y="0" width="22" height="22" rx="3"/>
        <path class="tick-icon" d="M5 11 L11 17 L25 -2"/>
      </g>
      <text class="service-item" x="100" y="101">NEW BUILDS</text>
      <g transform="translate(64,134)">
        <rect class="tick-icon" x="0" y="0" width="22" height="22" rx="3"/>
        <path class="tick-icon" d="M5 11 L11 17 L25 -2"/>
      </g>
      <text class="service-item" x="100" y="159">RENOVATIONS</text>
      <g transform="translate(64,191)">
        <rect class="tick-icon" x="0" y="0" width="22" height="22" rx="3"/>
        <path class="tick-icon" d="M5 11 L11 17 L25 -2"/>
      </g>
      <text class="service-item" x="100" y="216">RESIDENTIAL</text>
      <g transform="translate(64,249)">
        <rect class="tick-icon" x="0" y="0" width="22" height="22" rx="3"/>
        <path class="tick-icon" d="M5 11 L11 17 L25 -2"/>
      </g>
      <text class="service-item" x="100" y="274">COMMERCIAL</text>
    </g>

    <g class="contact-block">
      <path class="phone-icon" transform="translate(60,474) scale(1.5)"
            d="M6.6 10.8c1.4 2.8 3.8 5.1 6.6 6.6l2.2-2.2c.3-.3.7-.4 1-.2 1.1.4 2.3.6 3.6.6.6 0 1 .4 1 1V20c0 .6-.4 1-1 1C10.6 21 3 13.4 3 4c0-.6.4-1 1-1h3.5c.6 0 1 .4 1 1 0 1.3.2 2.5.6 3.6.1.3 0 .7-.2 1L6.6 10.8z"/>
      <text class="phone-number" x="101" y="511">0493 518 264</text>
      <rect class="contact-rule" x="64" y="528" width="9" height="62" fill="var(--bronze)"/>
      <text class="contact-line" x="86" y="551">rbrentconstruction.example.net</text>
      <text class="contact-line" x="86" y="583">rbrentconstruction@mailbox-example.net</text>
    </g>

    <g class="company-block">
      <text class="company-name" x="830" y="380" text-anchor="middle">R Brent</text>
      <text class="company-name" x="830" y="456" text-anchor="middle">Construction</text>
    </g>
  </svg>
</div>
</body>
</html>
```